create a Wedding Invitation design

Personalized wedding invitation using names, initials, a nice monogram with decorative border

incorporate names: Lena and Gordon (first names)
Holbeck (surname)
and wedding date , April 12, 2014

Colors: black ink on white;
optional accent colors: bright pink, bright orange, cajun red (may be flowers)
No shades of Purple

Industry/Entity Type

Wedding

Requirements
Must have
• Romantic, slightly formal looking design, black on white ; some accent color preferred, monogram (using first names Lena and Gordon and last name Holbeck), that could be isolated and used on RSVP cards preferred
Nice to have
• idea of being at the top of a building (venue is called Marlow Hall) - the wedding is being held on the 17th floor of building with panoramic views of Washington DC and the mountains ; Washington DC skyline, iconic DC cherry blossoms

Here are some examples of a typical Washington, DC skyline (this is an optional or secondary feature only - not to dominate the design):
http://www.pictavault.example/clip-art/washington-dc.html#comp.asp?recid=48113706&xtra=
Cherry blossoms : http://www.roamlyguide.example/news/story_8614.html

```html
<!DOCTYPE html>
<html lang="en">
<head>
<meta charset="utf-8">
<title>Lena and Gordon Holbeck – Wedding Invitation</title>
<link rel="stylesheet" href="https://fonts.googleapis.com/css2?family=Cormorant+Garamond:ital,wght@1,500&family=Crimson+Pro:wght@400&display=swap">
<style>
  :root {
    --ink: #111111;
    --paper: #ffffff;
    --accent-red: #c0141c;
    --sky-top: #1f5fd0;
    --sky-low: #8fb8e8;
    --skyline: #6f8a6a;
    --blossom: #d98fb8;
    --water-top: #3a6fb0;
    --water-low: #1d3f78;
  }
  html, body {
    margin: 0;
    padding: 0;
    overflow: hidden;
    background: var(--paper);
  }
  .invitation {
    position: relative;
    width: 1200px;
    height: 849px;
    background: var(--paper);
    color: var(--ink);
    font-family: "Crimson Pro", Georgia, serif;
    overflow: hidden;
  }
  .script {
    font-family: "Cormorant Garamond", "Times New Roman", serif;
    font-style: italic;
    font-weight: 500;
    margin: 0;
    position: absolute;
    left: 100px;
    line-height: 1;
    white-space: nowrap;
  }
  .host-name { font-size: 66px; }
  .host-first { top: 76px; }
  .host-second { top: 212px; }
  .event-title { font-size: 46px; top: 352px; }
  .line {
    position: absolute;
    left: 100px;
    margin: 0;
    font-size: 27px;
    line-height: 33px;
    white-space: nowrap;
  }
  .connector { top: 156px; }
  .invite-line { top: 298px; }
  .event-when { top: 438px; }
  .event-venue { top: 534px; }
  .rsvp {
    position: absolute;
    left: 796px;
    top: 512px;
    margin: 0;
    font-size: 27px;
    line-height: 33px;
  }
  .monogram {
    position: absolute;
    left: 940px;
    top: 62px;
    width: 188px;
    height: 232px;
    display: flex;
    align-items: center;
    justify-content: center;
    text-align: center;
    font-size: 20px;
    line-height: 26px;
    color: var(--accent-red);
  }
  .skyline-panorama {
    position: absolute;
    left: 0;
    top: 584px;
    width: 1200px;
    height: 236px;
    display: block;
  }
</style>
</head>
<body>
<main class="invitation">
  <h1 class="script host-name host-first">Lena Holbeck</h1>
  <p class="line connector">and</p>
  <h1 class="script host-name host-second">Gordon Holbeck</h1>
  <p class="line invite-line">invite you to share in their</p>
  <h2 class="script event-title">Wedding Celebration</h2>
  <p class="line event-when">Saturday, 12 th April 2014<br>at 7.00 p.m.</p>
  <p class="line event-venue">Venue: Any Hotel (Address)</p>
  <p class="rsvp">RSVP date<br>phone &nbsp;/ email</p>

  <div class="monogram">Lena Holbeck<br>Gordon Holbeck</div>

  <svg class="skyline-panorama" role="img" aria-label="Panorama of the Washington DC skyline across the water with cherry blossoms along the shore" viewBox="0 0 1200 236" preserveAspectRatio="none">
    <defs>
      <linearGradient id="panorama-tones" x1="0" y1="0" x2="0" y2="1">
        <stop offset="0" stop-color="var(--sky-top)"/>
        <stop offset="0.5" stop-color="var(--sky-low)"/>
        <stop offset="0.56" stop-color="var(--skyline)"/>
        <stop offset="0.64" stop-color="var(--blossom)"/>
        <stop offset="0.68" stop-color="var(--water-top)"/>
        <stop offset="1" stop-color="var(--water-low)"/>
      </linearGradient>
    </defs>
    <rect width="1200" height="236" fill="url(#panorama-tones)"/>
  </svg>
</main>
</body>
</html>
```